Norwegian psychologist service needs a fresh and exiting web site*

Norwegian psychologist service: working with therapy, personal development, mastery and personal growth. Focus: children and teenagers with special needs; family dynamics; group processes; individuals with a need for therapy and personal growth. (Our company name: Fjordlys og samhold (means Mastery and Growth).

We already have a logo for the company, which will be used (will be attached in the project).

The webside is to be structured in 4 pages with roll down curtain menus (the numbers are just for guiding the designer - the should not be added):

Page 1: Om Fjordlys og Samhold (about Mastery and Growth): this is where our business is is presented/described shortly: Lorem Ipsum dolor cit...

Page 2: Tjenester (Services): this is where our 5 service areas are presented:
2.1 Utredning (Investigation, diagnosing): Lorem Ipsum dolor cit...
2.2 Rådgivning (consulting): Lorem Ipsum dolor cit...

2.3 Kurs og work shops (courses and work shops): Lorem Ipsum dolor cit...
2.3a Fjordlys og samhold Tema 1 (T1)
2.3b Fjordlys og samhold Tema 2 (T2)
2.3c Fjordlys og samhold Tema 3 (T3)

2.4 Terapi og utvikling (Therapy and development)
2.4a Fjordlys og samhold for individer (FS1)
2.4b Fjordlys og samhold i familier (FS2)
2.4c Fjordlys og samhold i grupper (FS3)
2.4d Fjordlys og samhold i institusjoner (FS4)

Page 3: Aktuelt (Blog): this is our blog where we share knowledge and articles

Page 4: Kontakt (Contact): This is the contact form page. Contact form should constitute:
- Ditt navn (your name)
- E-post (your e-mail)
- Emne (subject)
- Melding (message/description)

Our project should also include suggestion for handheld units (iPhone, iPad).
Updates

We have both been traveling with work for a while, and then unfortunately both of us got sick on return, so we need a few more days to evaluate and choose design. Kind Regards Arvid & Margit

Target Market(s)

Focus on therapy, learning, mastery and growth for children and teenagers with special needs, within the family dynamics, or in a group setting.
OUR MARKETS:
Private market: individuals, families, groups and health industry institutions (with focus on learning, mastery, growth (as well as growing up) and psychiatry for children and teenagers with special difficulties and needs)
Public institutions: Government institutions, state institutions and municipality institutions (e.g. schools, municipality health service, hospitals) that serve the public (families with children and teenagers with special needs, and where learning, mastery, growth (as well as growing up) and potential psychiatry is an issue).

Number of Pages Required

4 page

Font styles to use
Sans Serif

Colors

Designer to choose colors to be used in the design.

Requirements
Must have
• The website must have 4 pages with roll down curtain menus (we have added a PDF with suggested structure, and headings, with sub menus - see attached PDF drawing.
• The web page must also use the added logo file - and make the web page work well with our logo.
• We would like the website to have a modern look and we would like the site to be associated with typical HIGH END TOP QUALITY private health institutions, but with a stronger focus on human beings (hands, faces etc), and not white coats and doctors. We are psychologists in the private market.
• For instance, if photos are being used - we tend to like "warm" almost art-like, "grainy" two-tone (e.g. sepia) photos to illustrate our focus. If designer can find such photos as part of design, it would be interesting to us. We would like a few photos like that integrated in the design.
• We also want a design suggestion for how the web page should look like and behave on handheld units (e.g. iPhone, iPad).
Nice to have
• If designer could find a number of suitable photos that matches the business idea and design requirements (see description above), that could follow website, that would be good.
• It could also be nice to have graphic symbols that denote the different pages/subpages (subjects)....
• HORSES: we sometimes use horses as a "tool" in therapy sessions. The horse is not necessarily used for riding, but for contact, communication and grooming. PHOTOS: we would like the designer to find an opportunity for using a photo reflecting this cooperation between therapist, child, teenager and horse. It is a bit up to the designer to find a way to do this... Since the horse is only a tool, among many other tools, it does not have to be much - but we want to try and see how it will work with a photo that also reflects this part of our business.

```html
<!DOCTYPE html>
<html lang="no">
<head>
<meta charset="utf-8">
<title>Fjordlys og Samhold</title>
<link href="https://fonts.googleapis.com/css2?family=Jost:wght@300;400;500;600;700&display=swap" rel="stylesheet">
<style>
:root{
  --green:#0e6b2f;
  --green-dark:#0a5424;
  --blue:#3d47a3;
  --blue-deep:#25308e;
  --ink:#1d1d1d;
  --text:#4a4a4a;
  --muted:#f4f4f7;
  --white:#ffffff;
  --line:#cfcfd6;
}
*{margin:0;padding:0;box-sizing:border-box}
html,body{width:1200px;height:3623px;overflow:hidden}
body{position:relative;font-family:'Jost',sans-serif;color:var(--ink);background:var(--white)}
.abs{position:absolute}
.photo{position:absolute}

/* hero */
.hero{position:absolute;left:0;top:0;width:1200px;height:575px;overflow:hidden}
.hero-photo{inset:0;background:
  radial-gradient(ellipse 260px 220px at 90px 470px,#b8382e 0%,rgba(184,56,46,0) 100%),
  radial-gradient(ellipse 220px 260px at 330px 380px,#9a6a4c 0%,rgba(154,106,76,0) 100%),
  radial-gradient(ellipse 200px 200px at 280px 140px,#d9a98a 0%,rgba(217,169,138,0) 100%),
  radial-gradient(ellipse 300px 260px at 980px 380px,#e8d8c4 0%,rgba(232,216,196,0) 100%),
  radial-gradient(ellipse 200px 160px at 620px 520px,#4c5d78 0%,rgba(76,93,120,0) 100%),
  linear-gradient(100deg,#8a5a42 0%,#b98c6c 35%,#cdb293 60%,#b7a28c 80%,#8f7a6a 100%)}
.hero-shade{position:absolute;inset:0;background:linear-gradient(rgba(20,20,40,.28),rgba(20,20,40,.38))}
.brand{position:absolute;display:flex;align-items:center;gap:8px;color:var(--white);font-weight:500;letter-spacing:.5px}
.brand-dot{width:14px;height:14px;border-radius:50%;background:var(--white)}
.hero .brand{left:150px;top:40px;font-size:14px}
.nav-item{position:absolute;top:40px;font-size:12px;color:var(--white);display:flex;align-items:center;gap:5px;white-space:nowrap}
.caret{width:0;height:0;border-left:5px solid transparent;border-right:5px solid transparent;border-top:5px solid var(--white)}
.cta-top{position:absolute;left:841px;top:32px;width:110px;height:34px;border-radius:4px;background:var(--blue-deep);color:var(--white);font-size:12px;display:flex;align-items:center;justify-content:center;box-shadow:0 2px 5px rgba(0,0,0,.3)}
.hero-title{position:absolute;left:0;width:1200px;top:222px;text-align:center;color:var(--white);font-size:43px;font-weight:400;letter-spacing:.5px}
.hero-text{position:absolute;left:290px;width:620px;top:292px;text-align:center;color:var(--white);font-size:12.5px;line-height:24px}
.btn-green{position:absolute;background:var(--green);color:var(--white);font-size:12.5px;border-radius:4px;display:flex;align-items:center;justify-content:center;box-shadow:0 3px 6px rgba(0,0,0,.25)}
.arrow{position:absolute;width:42px;height:42px;border-radius:50%;background:#1f1f2a;border:2px solid #d8d8e0;display:flex;align-items:center;justify-content:center}
.arrow svg{width:16px;height:16px}

/* about */
.about-photo{left:176px;top:636px;width:366px;height:366px;border-radius:50%;border:3px solid var(--green);padding:6px;background:var(--white)}
.about-photo div{width:100%;height:100%;border-radius:50%;background:
  radial-gradient(ellipse 70px 80px at 45% 25%,#d9b39a 0%,rgba(217,179,154,0) 100%),
  radial-gradient(ellipse 130px 150px at 45% 65%,#f6f5f2 0%,rgba(246,245,242,0) 100%),
  linear-gradient(90deg,#b8b2aa 0%,#dcd8d2 40%,#c7c0b6 75%,#9d938a 100%)}
.h2{position:absolute;font-weight:400;color:var(--ink)}
.rule{position:absolute;height:3px;background:var(--ink)}
.about-text{position:absolute;left:590px;top:724px;width:440px;font-size:11.5px;line-height:26.6px;color:var(--text)}

/* services */
.services{position:absolute;left:0;top:1066px;width:1200px;height:659px;background:var(--blue)}
.services-photo{position:absolute;left:0;top:0;width:620px;height:659px;background:radial-gradient(ellipse at 35% 35%,rgba(110,110,190,.7),rgba(61,71,163,0) 70%)}
.service{position:absolute;width:300px;text-align:center;color:var(--white)}
.service-circle{position:relative;width:220px;height:220px;margin:0 auto;border-radius:50%;overflow:hidden}
.c1{background:radial-gradient(ellipse 60px 80px at 30% 45%,#f2f2f2 0%,rgba(242,242,242,0) 100%),linear-gradient(160deg,#b0553e 0%,#d9cbbd 45%,#c7b9a8 70%,#6d6159 100%)}
.c2{background:radial-gradient(ellipse 70px 50px at 55% 50%,#e8e4de 0%,rgba(232,228,222,0) 100%),linear-gradient(160deg,#2e2e33 0%,#6b5848 40%,#b48c6c 65%,#4b4c55 100%)}
.c3{background:radial-gradient(ellipse 60px 70px at 70% 50%,#e6a8b8 0%,rgba(230,168,184,0) 100%),radial-gradient(ellipse 70px 70px at 30% 70%,#7b9fc8 0%,rgba(123,159,200,0) 100%),linear-gradient(160deg,#d8c4a8 0%,#c9a384 50%,#e2d6c4 100%)}
.service-icon{position:absolute;left:60px;bottom:-50px;width:100px;height:100px;border-radius:50%;background:var(--green);display:flex;justify-content:center;padding-top:14px}
.service h3{font-weight:400;font-size:25px;margin-top:22px}
.service p{font-size:11.5px;line-height:23.5px;margin-top:12px}
.btn-ghost{display:inline-block;margin-top:20px;width:77px;height:34px;line-height:32px;border:1px solid var(--white);border-radius:5px;font-size:11.5px}

/* testimonials */
.center{position:absolute;left:0;width:1200px;text-align:center}
.quote-text{position:absolute;left:360px;width:540px;top:1932px;text-align:center;font-size:12px;line-height:24px;color:var(--text)}
.qmark{position:absolute;font-size:110px;font-weight:700;color:var(--blue-deep);line-height:1;font-family:Georgia,serif}
.small-arrow{position:absolute;width:36px;height:36px;border-radius:50%;background:var(--white);box-shadow:0 2px 8px rgba(0,0,0,.15);display:flex;align-items:center;justify-content:center}
.avatar{position:absolute;left:560px;top:2024px;width:80px;height:80px;border-radius:50%;background:radial-gradient(circle at 50% 45%,#f0d6c4 0%,#c48a66 55%,#6e4a35 100%)}

/* news */
.news{position:absolute;left:0;top:2220px;width:1200px;height:622px;background:var(--muted)}
.card{position:absolute;top:2414px;width:290px;height:359px;background:var(--white);box-shadow:0 2px 10px rgba(0,0,0,.08);padding:10px}
.card-photo{width:270px;height:176px}
.p1{background:radial-gradient(ellipse 60px 70px at 45% 40%,#5a3a2c 0%,rgba(90,58,44,0) 100%),linear-gradient(135deg,#e9e6e0 0%,#d3cec6 50%,#8a8a7a 100%)}
.p2{background:radial-gradient(ellipse 60px 60px at 65% 55%,#7ea7cf 0%,rgba(126,167,207,0) 100%),linear-gradient(135deg,#c7b49a 0%,#e8e3dc 45%,#d7d1c8 100%)}
.p3{background:radial-gradient(ellipse 60px 70px at 40% 45%,#6b4634 0%,rgba(107,70,52,0) 100%),linear-gradient(135deg,#eeece8 0%,#dcd6cf 55%,#f4f2ee 100%)}
.card h4{font-weight:400;font-size:20px;margin:20px 0 0 20px}
.card p{font-size:10.5px;line-height:18.5px;color:var(--text);margin:12px 20px 0 20px}
.card .more{font-size:10.5px;letter-spacing:1.5px;color:var(--green);font-weight:500;margin:12px 0 0 20px}

/* contact */
.field{position:absolute;left:236px;width:392px;border:1px solid var(--line);border-radius:4px;display:flex;align-items:flex-start;padding:18px 0 0 18px;gap:10px;font-size:11.5px;color:#9a9a9a}
.field svg{width:18px;height:18px}
.info-icon{position:absolute;left:681px;width:50px;height:50px;border-radius:50%;background:var(--green);display:flex;align-items:center;justify-content:center}
.info-icon svg{width:26px;height:26px}
.info{position:absolute;left:749px;font-size:12px;color:var(--ink)}
.social{position:absolute;top:3403px;width:30px;height:30px;border-radius:50%;background:var(--blue-deep)}

/* footer */
.footer{position:absolute;left:0;top:3526px;width:1200px;height:97px;background:var(--green)}
.footer-badge{position:absolute;left:142px;top:3492px;width:186px;height:186px;border-radius:50%;background:var(--white)}
.footer .copy{position:absolute;left:782px;top:42px;color:var(--white);font-size:11.5px}
</style>
</head>
<body>

<section class="hero">
  <div class="photo hero-photo" role="img" aria-label="Warm photo of a young girl holding a teddy bear while a therapist takes notes"></div>
  <div class="hero-shade"></div>
  <div class="brand"><span class="brand-dot"></span>FJORDLYS OG SAMHOLD</div>
  <nav>
    <span class="nav-item" style="left:422px">Home</span>
    <span class="nav-item" style="left:480px">Om Fjordlys og Samhold</span>
    <span class="nav-item" style="left:626px">Tjenester <i class="caret"></i></span>
    <span class="nav-item" style="left:703px">Aktuelt</span>
    <span class="nav-item" style="left:768px">Kontakt</span>
  </nav>
  <div class="cta-top">Be om avtale</div>
  <h1 class="hero-title">FJORDLYS OG SAMHOLD</h1>
  <p class="hero-text">Phasellus mattis sit amet ipsum ut posuere. Fusce in faucibus felis. Fusce lobortis lobortis erat vitae aliquet. Vestibulum sodales ultricies turpis, non dapibus sapien maximus vitae.</p>
  <div class="btn-green" style="left:547px;top:362px;width:110px;height:34px">Les mer</div>
  <div class="arrow" style="left:-4px;top:269px"><svg viewBox="0 0 16 16"><path d="M10 2 4 8l6 6" fill="none" stroke="#fff" stroke-width="2"/></svg></div>
  <div class="arrow" style="left:1161px;top:269px"><svg viewBox="0 0 16 16"><path d="m6 2 6 6-6 6" fill="none" stroke="#fff" stroke-width="2"/></svg></div>
</section>

<section class="about">
  <div class="abs about-photo"><div role="img" aria-label="Therapist seated with a clipboard in a bright consulting room"></div></div>
  <h2 class="h2" style="left:590px;top:646px;font-size:34px">Om Fjordlys og Samhold</h2>
  <div class="rule" style="left:590px;top:701px;width:67px"></div>
  <p class="about-text">Phasellus sem mi, aliquet mattis pulvinar eu, vestibulum a velit. Phasellus venenatis urna nulla, vitae ultrices tellus facilisis in. Duis at placerat enim. Morbi ultrices dolor quis dolor ultrices accumsan eget ac odio. Nam ornare varius est, a molestie eros vestibulum eget. Nulla vel odio id tortor tincidunt ultricies quis at magna. Donec pellentesque imperdiet sagittis. Etiam ut hendrerit purus. Mauris suscipit dolor non est egestas, id dapibus tortor rutrum. Praesent eu magna eget augue mollis egestas vel non lacus. Donec et sapien ut nibh iaculis consequat non vitae ex. Donec cursus elementum pellentesque. Mauris non molestie risus.</p>
  <div class="btn-green" style="left:590px;top:954px;width:110px;height:34px">Les mer</div>
</section>

<section class="services">
  <div class="services-photo" role="img" aria-label="Faint photo of a smiling woman behind the blue tint"></div>
  <h2 class="center" style="top:56px;font-size:34px;font-weight:400;color:#fff">Tjenester</h2>
  <div class="abs" style="left:566px;top:113px;width:67px;height:3px;background:#fff"></div>

  <div class="service" style="left:136px;top:172px">
    <div class="service-circle c1" role="img" aria-label="Therapist in conversation with a client on a sofa">
      <div class="service-icon"><svg width="30" height="30" viewBox="0 0 30 30"><rect x="6" y="5" width="18" height="22" rx="2" fill="none" stroke="#fff" stroke-width="2"/><rect x="11" y="2" width="8" height="5" rx="1" fill="#fff"/><path d="M10 14h10M10 18h10M10 22h6" stroke="#fff" stroke-width="1.6"/></svg></div>
    </div>
    <h3>Utredning</h3>
    <p>Cras porttitor metus vel hendrerit sagittis.<br>Suspendisse ornare, eros eget tincidunt efficitur,<br>augue lorem condimentum magna</p>
    <span class="btn-ghost">Les mer</span>
  </div>
  <div class="service" style="left:450px;top:172px">
    <div class="service-circle c2" role="img" aria-label="Hands of a client and a counsellor with a clipboard">
      <div class="service-icon"><svg width="30" height="30" viewBox="0 0 30 30"><circle cx="15" cy="8" r="4" fill="none" stroke="#fff" stroke-width="2"/><path d="M7 20c0-4 4-6 8-6s8 2 8 6" fill="none" stroke="#fff" stroke-width="2"/><rect x="5" y="21" width="20" height="5" fill="#fff"/></svg></div>
    </div>
    <h3>Rådgivning</h3>
    <p>Cras porttitor metus vel hendrerit sagittis.<br>Suspendisse ornare, eros eget tincidunt efficitur,<br>augue lorem condimentum magna</p>
    <span class="btn-ghost">Les mer</span>
  </div>
  <div class="service" style="left:765px;top:172px">
    <div class="service-circle c3" role="img" aria-label="Mother and daughter playing together on the floor">
      <div class="service-icon"><svg width="30" height="30" viewBox="0 0 30 30"><rect x="4" y="6" width="22" height="18" rx="2" fill="none" stroke="#fff" stroke-width="2"/><path d="M15 6v18M8 11h4M8 15h4M18 11h4M18 15h4" stroke="#fff" stroke-width="1.6"/></svg></div>
    </div>
    <h3>Kurs og work shops</h3>
    <p>Cras porttitor metus vel hendrerit sagittis.<br>Suspendisse ornare, eros eget tincidunt efficitur,<br>augue lorem condimentum magna</p>
    <span class="btn-ghost">Les mer</span>
  </div>

  <div class="arrow" style="left:-4px;top:308px"><svg viewBox="0 0 16 16"><path d="M10 2 4 8l6 6" fill="none" stroke="#fff" stroke-width="2"/></svg></div>
  <div class="arrow" style="left:1161px;top:308px"><svg viewBox="0 0 16 16"><path d="m6 2 6 6-6 6" fill="none" stroke="#fff" stroke-width="2"/></svg></div>
</section>

<section class="testimonials">
  <h2 class="center" style="top:1776px;font-size:34px;font-weight:400">Uttalelser</h2>
  <p class="center" style="top:1832px;font-size:15px;font-weight:300;color:var(--text)">Omtaler av vår fornøyde kunde</p>
  <div class="rule" style="left:566px;top:1866px;width:67px"></div>
  <div class="small-arrow" style="left:190px;top:1942px"><svg width="12" height="12" viewBox="0 0 12 12"><path d="M8 1 3 6l5 5" fill="none" stroke="#25308e" stroke-width="1.8"/></svg></div>
  <div class="small-arrow" style="left:975px;top:1942px"><svg width="12" height="12" viewBox="0 0 12 12"><path d="m4 1 5 5-5 5" fill="none" stroke="#25308e" stroke-width="1.8"/></svg></div>
  <div class="qmark" style="left:296px;top:1886px">&ldquo;</div>
  <div class="qmark" style="left:828px;top:1980px">&rdquo;</div>
  <p class="quote-text">Suspendisse faucibus pellentesque neque ac bibendum. Nullam viverra justo ultrices, tincidunt enim nec, congue turpis. Pellentesque suscipit nunc sem, ac congue erat semper vel. In sed velit elementum dolor posuere mattis vel dictum augue. Morbi ac metus a tortor elementum eleifend.</p>
  <div class="avatar" role="img" aria-label="Portrait of the client"></div>
  <p class="center" style="top:2119px;font-size:17px;font-weight:600">Navn her</p>
  <p class="center" style="top:2147px;font-size:13px;font-weight:300;color:var(--text)">klient</p>
</section>

<section class="news">
  <h2 class="center" style="top:66px;font-size:34px;font-weight:400">Aktuelt</h2>
  <p class="center" style="top:119px;font-size:15px;font-weight:300;color:var(--text)">dette er bloggen vår hvor vi deler kunnskap og artikler</p>
  <div class="rule" style="left:566px;top:152px;width:67px"></div>
</section>
<article class="card" style="left:142px">
  <div class="card-photo p1" role="img" aria-label="Worried young woman resting her head on her hand"></div>
  <h4>Tittel her</h4>
  <p>Duis placerat viverra nisl, ac tristique augue aliquet at. Praesent malesuada orci et magna luctus, quis mollis orci rhoncus</p>
  <div class="more">READ MORE</div>
</article>
<article class="card" style="left:455px">
  <div class="card-photo p2" role="img" aria-label="Counsellor taking notes beside a teenage girl on a sofa"></div>
  <h4>Tittel her</h4>
  <p>Duis placerat viverra nisl, ac tristique augue aliquet at. Praesent malesuada orci et magna luctus, quis mollis orci rhoncus</p>
  <div class="more">READ MORE</div>
</article>
<article class="card" style="left:768px">
  <div class="card-photo p3" role="img" aria-label="Smiling woman talking with a therapist holding a clipboard"></div>
  <h4>Tittel her</h4>
  <p>Duis placerat viverra nisl, ac tristique augue aliquet at. Praesent malesuada orci et magna luctus, quis mollis orci rhoncus</p>
  <div class="more">READ MORE</div>
</article>

<section class="contact">
  <h2 class="center" style="top:2894px;font-size:34px;font-weight:400;left:-2px">Kontakt</h2>
  <div class="field" style="top:3032px;height:56px"><svg viewBox="0 0 18 18"><circle cx="9" cy="6" r="3.5" fill="none" stroke="#aaa"/><path d="M2 17c0-4 3-6 7-6s7 2 7 6" fill="none" stroke="#aaa"/></svg>Ditt navn</div>
  <div class="field" style="top:3099px;height:56px"><svg viewBox="0 0 18 18"><rect x="1" y="4" width="16" height="11" fill="none" stroke="#aaa"/><path d="m1 4 8 6 8-6" fill="none" stroke="#aaa"/></svg>E-post</div>
  <div class="field" style="top:3165px;height:56px"><svg viewBox="0 0 18 18"><path d="m9 1.5 2.3 4.8 5.2.7-3.8 3.6.9 5.2L9 13.3l-4.6 2.5.9-5.2L1.5 7l5.2-.7z" fill="none" stroke="#aaa"/></svg>Emne</div>
  <div class="field" style="top:3232px;height:121px"><svg viewBox="0 0 18 18"><path d="m3 15 1-4 9-9 3 3-9 9z" fill="none" stroke="#aaa"/></svg>Melding</div>
  <div class="btn-green" style="left:236px;top:3377px;width:133px;height:39px;font-size:15px;font-weight:600;box-shadow:none">Sende inn</div>

  <div class="info-icon" style="top:3032px"><svg viewBox="0 0 26 26"><path d="M13 24s-7-8-7-13a7 7 0 0 1 14 0c0 5-7 13-7 13z" fill="none" stroke="#fff" stroke-width="1.6"/><circle cx="13" cy="11" r="2.5" fill="none" stroke="#fff" stroke-width="1.6"/></svg></div>
  <p class="info" style="top:3036px;font-weight:600">Fjordlys Og Samhold</p>
  <p class="info" style="top:3060px">123Integer malesuada in dui varius viverra</p>
  <div class="info-icon" style="top:3127px"><svg viewBox="0 0 26 26"><path d="M6 4h4l2 5-3 2c1 3 3 5 6 6l2-3 5 2v4c0 1-1 2-2 2C11 22 4 15 4 6c0-1 1-2 2-2z" fill="none" stroke="#fff" stroke-width="1.6"/></svg></div>
  <p class="info" style="top:3142px;font-weight:600;font-size:13px">22-40-1177</p>
  <div class="info-icon" style="top:3217px"><svg viewBox="0 0 26 26"><rect x="3" y="6" width="20" height="14" fill="none" stroke="#fff" stroke-width="1.6"/><path d="m3 6 10 8 10-8M3 20l7-6M23 20l-7-6" fill="none" stroke="#fff" stroke-width="1.6"/></svg></div>
  <p class="info" style="top:3234px">post@fjordlys-samhold.no</p>

  <p class="info" style="left:681px;top:3336px;font-size:20px;font-weight:700">Follow Me</p>
  <span class="social" style="left:681px"></span>
  <span class="social" style="left:731px"></span>
  <span class="social" style="left:777px"></span>
</section>

<footer class="footer">
  <p class="copy">© COPYRIGHT 2020 FJORDLYS OG SAMHOLD</p>
</footer>
<div class="footer-badge"></div>
<div class="brand" style="left:158px;top:3558px;color:var(--blue-deep);font-size:14px;width:160px;justify-content:center;flex-direction:column;gap:6px;text-align:center;line-height:1.2">
  <span class="brand-dot" style="background:var(--green)"></span>FJORDLYS OG SAMHOLD
</div>

</body>
</html>
```